Remote Computer Support PostCard

We need a Postcard Ad for marketing to businesses that need Remote Computer Support and Security. 2 sided and able to be mailed. Can be any color but color we use mostly is red. Remote Computer Support and Security per PC. Includes Remote Monitoring and Maintenance(RMM) Agent, Business Security Tools including Antivirus, Anti Malware, Ransomware Protection, Intrusion Prevention, Content Filtering and others. All remote support you need for $69.99 per pc per month.

Target Market(s)

All Businesses

Industry/Entity Type

Computer Support for Businesses

Colors
EB3D1F
EC4F4E
F09395
F8D3D4
FCEDEE

Requirements
Must have
• BrivoLane, Inc. (555) 246-9137 . Sales@brivolane.example. Designed to be mailed. 6x9 Postcard Mailer Size Final 6.25" x 9" Ink & Bleed Four Color Process, Full Bleed Two Sides. Must have places for postage.
Nice to have
• Main lines should be in top 1/3 of postcard to stand out in mail.

```html
<!DOCTYPE html>
<html lang="en">
<head>
<meta charset="utf-8">
<title>BrivoLane Remote Support Postcard</title>
<link rel="stylesheet" href="https://fonts.googleapis.com/css2?family=Anton&family=Montserrat:wght@500;600;700;800&family=Red+Hat+Display:wght@900&display=swap">
<style>
  :root{
    --red:#d41f26;
    --red-dark:#9e1218;
    --black:#0b0c10;
    --white:#ffffff;
    --yellow:#f4ec00;
    --ink:#1a1a1a;
    --stage:#dcdcdc;
    --stamp:#8a8c90;
    --rule:#c4c4c4;
  }
  *{box-sizing:border-box;margin:0;padding:0}
  html,body{width:1200px;height:1117px;overflow:hidden;background:var(--stage)}
  body{position:relative;font-family:"Montserrat",sans-serif;color:var(--ink)}

  .postcard{position:absolute;width:760px;height:528px;background:var(--white);overflow:hidden;box-shadow:0 6px 18px rgba(0,0,0,.25)}
  .postcard--front{left:40px;top:24px}
  .postcard--back{left:400px;top:565px}
  .postcard__shapes{position:absolute;inset:0;width:760px;height:528px}
  .abs{position:absolute}

  .brand{display:flex;align-items:center;gap:10px;font-family:"Montserrat",sans-serif;font-weight:800;color:var(--black);letter-spacing:-1px;line-height:1;white-space:nowrap}
  .brand__mark{width:16px;height:16px;background:var(--red)}

  /* front */
  .front-brand{left:58px;top:52px;font-size:46px}
  .headline{left:66px;top:158px;font-family:"Anton",sans-serif;color:var(--white);line-height:1.02}
  .headline__lead{font-size:52px;display:block}
  .headline__line{font-size:36px;display:block}
  .headline__accent{font-size:60px;display:block;color:var(--yellow)}

  .offer{left:56px;top:372px;color:var(--white)}
  .offer__label{font-size:16px;font-weight:700;letter-spacing:.5px}
  .offer__price{display:flex;align-items:flex-end;gap:8px;margin-top:-2px}
  .offer__amount{font-family:"Red Hat Display",sans-serif;font-weight:900;font-size:74px;line-height:.95;letter-spacing:-1px}
  .offer__unit{font-size:12px;font-weight:600;margin-bottom:30px}
  .offer__note{font-size:11.5px;font-weight:700;line-height:1.35;margin-top:6px;width:360px;text-transform:uppercase}

  .check-list{list-style:none}
  .check-list li{position:relative;padding-left:20px}
  .check-list li::before{content:"";position:absolute;left:2px;top:.38em;width:9px;height:4.5px;border-left:2.5px solid currentColor;border-bottom:2.5px solid currentColor;transform:rotate(-45deg)}

  .features{left:498px;top:356px;width:250px;font-size:12.5px;font-weight:600;line-height:22px;color:var(--ink);text-transform:uppercase}

  /* back */
  .back-title{left:50px;top:34px;font-family:"Anton",sans-serif;font-size:32px;color:var(--white);line-height:1}
  .back-title span{color:var(--yellow)}
  .back-title__rule{left:52px;top:80px;width:64px;height:2px;background:var(--white)}
  .back-intro{left:46px;top:92px;width:340px;font-size:12px;font-weight:500;line-height:1.4;color:var(--white)}
  .back-intro li{margin-bottom:2px}

  .setup{left:58px;top:190px;width:340px;font-size:14px;font-weight:800;line-height:1.25;color:var(--white);text-transform:uppercase}
  .setup span{color:var(--yellow);display:block}

  .includes{left:50px;top:246px;width:380px}
  .includes__title{font-size:17px;font-weight:800;color:var(--red);line-height:1.2}
  .includes__list{list-style:none;font-size:12px;font-weight:500;line-height:1.35;margin-top:1px}
  .includes__list li::before{content:"\2022\00a0"}

  .tools{font-size:10px;font-weight:600;line-height:11.6px;color:var(--white)}
  .tools li{padding-left:16px}
  .tools li::before{width:7px;height:3.5px;border-width:2px;top:.3em}
  .tools--a{left:40px;top:344px;width:180px}
  .tools--b{left:228px;top:332px;width:200px}

  .contact{left:56px;top:466px;color:var(--white)}
  .contact__phone{display:flex;align-items:center;gap:8px;font-family:"Anton",sans-serif;font-size:34px;line-height:1}
  .contact__email{font-size:13px;font-weight:500;margin:4px 0 0 40px}

  .back-brand{left:446px;top:60px;font-size:30px;gap:8px}
  .back-brand .brand__mark{width:12px;height:12px}
  .stamp{left:652px;top:28px;width:80px;height:90px;background:var(--stamp)}
  .address-lines{left:494px;top:250px;width:246px}
  .address-lines span{display:block;height:1px;background:var(--rule);margin-bottom:38px}
</style>
</head>
<body>

<section class="postcard postcard--front" aria-label="Postcard front">
  <svg class="postcard__shapes" viewBox="0 0 760 528">
    <defs>
      <linearGradient id="photoTone" x1="0" y1="0" x2="1" y2="1">
        <stop offset="0" stop-color="#0b1a3a"/>
        <stop offset=".5" stop-color="#1f5fb8"/>
        <stop offset="1" stop-color="#0a2450"/>
      </linearGradient>
    </defs>
    <polygon points="0,140 300,140 325,55 412,55 382,175 455,355 0,355" fill="var(--black)"/>
    <polygon role="img" aria-label="Photo: hands typing on a laptop keyboard with glowing cyber security lock and network overlay" points="459,0 760,0 760,322 480,322 415,175" fill="url(#photoTone)"/>
    <polyline points="436,0 392,175 465,355" fill="none" stroke="var(--red)" stroke-width="9"/>
    <polyline points="449,0 405,175 474,330" fill="none" stroke="var(--red-dark)" stroke-width="4"/>
    <polygon points="0,355 455,355 520,528 0,528" fill="var(--red)"/>
    <polygon points="0,355 455,355 462,372 0,372" fill="var(--red-dark)" opacity=".35"/>
    <rect x="0" y="516" width="760" height="12" fill="var(--red)"/>
  </svg>

  <div class="abs brand front-brand"><span>BrivoLane</span><span class="brand__mark"></span></div>

  <h1 class="abs headline">
    <span class="headline__lead">Finaly</span>
    <span class="headline__line">Computer Security</span>
    <span class="headline__line">and Support</span>
    <span class="headline__accent">Made Easy!</span>
  </h1>

  <div class="abs offer">
    <div class="offer__label">FOR ONLY</div>
    <div class="offer__price"><span class="offer__amount">$69.99/</span><span class="offer__unit">MONTH</span></div>
    <p class="offer__note">Per PC you can get world class security services and unlimited remote technical support.</p>
  </div>

  <ul class="abs check-list features">
    <li>Automated Vantix OS Updates</li>
    <li>Automated System Cleanup</li>
    <li>Monthly Reports</li>
    <li>Managed Antivirus Including</li>
    <li>Ransomware Detection And</li>
    <li>Protection</li>
  </ul>
</section>

<section class="postcard postcard--back" aria-label="Postcard back">
  <svg class="postcard__shapes" viewBox="0 0 760 528">
    <polygon points="0,0 425,0 400,205 0,205" fill="var(--black)"/>
    <polygon points="400,168 420,168 414,186 398,186" fill="var(--red-dark)"/>
    <polygon points="44,182 420,176 410,238 34,244" fill="var(--red)"/>
    <polygon points="0,322 405,322 452,392 418,462 0,462" fill="var(--red)"/>
    <polygon points="0,462 418,462 460,528 0,528" fill="var(--black)"/>
  </svg>

  <h2 class="abs back-title">AUTOMATED <span>REMOTE SUPPORT</span></h2>
  <div class="abs back-title__rule"></div>
  <ul class="abs check-list back-intro">
    <li>Remote monitoring and maintenance tools monitor your devices in real-time.</li>
    <li>Instantly informing you of current issues and flagging potential problems.</li>
  </ul>

  <p class="abs setup">One time setup fee of $69.99 then <span>only $69.99 per month per PC</span></p>

  <div class="abs includes">
    <div class="includes__title">Includes:</div>
    <ul class="includes__list">
      <li>Remote Monitoring and Management Agent (RMM)</li>
      <li>Help Desk Application on Desktop</li>
      <li>ShieldPoint Business Security</li>
    </ul>
  </div>

  <ul class="abs check-list tools tools--a">
    <li>ANTIVIRUS</li>
    <li>Real-Time Scan</li>
    <li>Scheduled Scan</li>
    <li>Manual Scan</li>
    <li>Behavior Monitoring</li>
    <li>Malware Behavior Blocking</li>
    <li>Ransomware Protection</li>
    <li>Anti-Exploit Protection</li>
    <li>LedgerPro Protection</li>
  </ul>
  <ul class="abs check-list tools tools--b">
    <li>Event Monitoring</li>
    <li>Firewall</li>
    <li>Vulnerability Protection</li>
    <li>Web Reputation</li>
    <li>Browser Exploit Prevention</li>
    <li>Predictive Machine Learning</li>
    <li>Device Control</li>
    <li>Data Loss Prevention</li>
    <li>URL Filtering</li>
    <li>Application Control</li>
  </ul>

  <div class="abs contact">
    <div class="contact__phone">
      <svg width="30" height="30" viewBox="0 0 30 30" aria-hidden="true">
        <circle cx="15" cy="15" r="15" fill="var(--yellow)"/>
        <path d="M10.5 8.5c.8-.6 1.7-.4 2.1.4l1.2 2.3c.3.6.1 1.3-.4 1.7l-.9.7c.7 1.6 2 2.9 3.6 3.6l.7-.9c.4-.5 1.1-.7 1.7-.4l2.3 1.2c.8.4 1 1.3.4 2.1l-.9 1.1c-.6.7-1.6 1-2.5.7-4.1-1.3-7.3-4.5-8.6-8.6-.3-.9 0-1.9.7-2.5z" fill="var(--black)"/>
      </svg>
      <span>(555) 246-9137</span>
    </div>
    <div class="contact__email">Sales@brivolane.example</div>
  </div>

  <div class="abs brand back-brand"><span>BrivoLane</span><span class="brand__mark"></span></div>
  <div class="abs stamp" aria-label="Postage area"></div>
  <div class="abs address-lines" aria-label="Address lines">
    <span></span><span></span><span></span><span></span><span></span><span></span>
  </div>
</section>

</body>
</html>
```